Web Design Project - KornHaus.de

The page shall provide individual brown-bread mix.
There shall be presented:
* RECIPES: consumer's choice and feedback area
* EQUIPMENT: baking equipment store
* BREAD-MIX: individual mix and configurator function for bread-mix
The consumer can search/view the content and checkout the products. A user can establish a profile. A user can interact on the page for feedback on content and connection to social media.
Industry/Entity Type
Store
Look and feel
Each slider illustrates characteristics of the customer's brand and the style your logo design should communicate.

```html
<!DOCTYPE html>
<html lang="en">
<head>
<meta charset="utf-8">
<title>KornHaus – Bread Mix Store</title>
<link rel="stylesheet" href="https://fonts.googleapis.com/css2?family=Sorts+Mill+Goudy&family=Marcellus&family=PT+Sans:wght@400;700&display=swap">
<style>
:root{
  --page:#efe6d3;
  --band:#ddd0b6;
  --brown:#7a4516;
  --brown-dark:#5a300d;
  --heading-red:#8b2d12;
  --price:#e8641c;
  --ink:#2b2118;
  --muted:#4a3b2c;
  --white:#ffffff;
  --frame:#6e3d12;
  --line:#cdbf9f;
  --serif:'Sorts Mill Goudy', Georgia, serif;
  --display:'Marcellus', Georgia, serif;
  --sans:'PT Sans', Arial, sans-serif;
}
*{box-sizing:border-box;margin:0;padding:0}
html,body{width:800px;height:1200px;overflow:hidden}
body{position:relative;background:var(--page);font-family:var(--sans);color:var(--ink)}
.abs{position:absolute}

.top-bar{left:0;top:0;width:800px;height:28px;background:var(--band)}
.top-bar .welcome{left:17px;top:7px;font-size:11px;color:var(--muted)}
.top-bar .account{right:26px;top:7px;font-size:11px;color:var(--muted);word-spacing:2px}
.account .sep{margin:0 10px}

.logo-banner{left:287px;top:0;width:232px;height:120px}
.logo-name{left:287px;top:22px;width:232px;text-align:center;font-family:var(--serif);font-size:30px;line-height:34px;color:var(--white);letter-spacing:1px}

.cart{left:26px;top:48px;display:flex;align-items:center;gap:14px;font-size:13px;color:var(--brown)}
.mini-search{left:64px;top:76px;width:118px;height:21px;background:var(--white);border-radius:6px;font-size:9px;color:#9a9a9a;padding:5px 9px}
.mini-search svg{position:absolute;right:3px;top:2px}

.search-label{left:557px;top:41px;font-size:19px;color:var(--brown)}
.search-field{left:556px;top:68px;width:219px;height:25px;background:var(--white)}
.search-btn{left:703px;top:99px;width:72px;height:21px;border-radius:5px;background:linear-gradient(#d8c8ac,#9b8666);border:1px solid #8a7458;font-size:13px;color:var(--ink);text-align:center;line-height:19px}

.main-nav{left:6px;top:130px;width:788px;height:32px;background:#e4d9c3;border-radius:6px;box-shadow:0 8px 8px -6px rgba(80,50,20,.35)}
.nav-item{position:absolute;top:0;height:32px;line-height:31px;font-family:var(--serif);font-size:15.5px;color:var(--ink);transform:translateX(-50%);white-space:nowrap}
.nav-item.active{background:var(--brown);color:var(--white);padding:0 12px;border-radius:3px;top:1px;height:30px;line-height:28px}

.hero{left:7px;top:186px;width:786px;height:328px;background:var(--white);overflow:hidden;box-shadow:0 6px 8px -4px rgba(80,50,20,.35)}
.hero-photo{left:0;top:0;width:373px;height:328px;background:radial-gradient(ellipse at 45% 45%,#d9a56a 0%,#a8652e 45%,#e9d6bb 100%)}
.hero-slices{left:535px;top:14px;width:240px;height:300px;background:radial-gradient(ellipse at 50% 55%,#f1e7d8 0%,#f7f1e8 60%,#ffffff 100%)}
.hero-title{left:403px;top:56px;font-family:var(--serif);font-weight:normal;font-size:41px;line-height:44px;color:var(--brown-dark);white-space:nowrap}
.hero-text{left:403px;top:97px;width:378px;font-family:var(--serif);font-size:15.4px;line-height:20.5px;color:var(--ink)}
.hero-price{left:401px;top:190px;font-family:var(--display);font-size:40px;line-height:44px;color:var(--price)}
.hero-arrows{left:403px;top:275px}
.ribbon{right:0;bottom:0}

.welcome-title{left:15px;top:541px;font-family:var(--serif);font-size:20px;font-weight:bold;color:var(--ink)}
.stay{left:504px;top:536px;width:269px;height:35px;background:#ddcfb3;border:1px solid #b4a07c;border-radius:3px}
.stay span{position:absolute;left:11px;top:5px;font-size:18px;color:var(--brown-dark)}
.social{position:absolute;top:4px;width:25px;height:25px;background:var(--brown);border-radius:3px}

.section-title{font-size:19px;font-weight:normal;color:var(--heading-red);white-space:nowrap}
.photo-frame{border:4px solid var(--frame);background:#fff}
.photo-fill{width:100%;height:100%}

.recipe-text{left:178px;top:621px;width:302px;font-size:10.1px;line-height:19px;color:var(--ink)}
.dark-btn{height:19px;border-radius:9px;background:linear-gradient(#5c5c5c,#1e1e1e);color:#fff;font-size:11px;text-align:center;line-height:17px;border:1px solid #888}
.v-line{width:1px;background:var(--line)}
.h-line{height:1px;background:var(--line)}
.pager{font-size:9px;color:var(--ink);letter-spacing:2px}
.thumb{width:74px;height:67px}

.mix{width:124px;height:113px}
.price-tab{position:absolute;left:50%;top:0;transform:translateX(-50%);width:58px;height:28px}
.price-tab b{position:absolute;left:0;top:3px;width:58px;text-align:center;font-family:var(--display);font-weight:normal;font-size:16px;color:#fff}

.label{font-size:11px;color:var(--ink)}
.field{background:#fff;border-radius:5px;width:167px}

.avatar{width:58px;height:50px;border-radius:3px;background:linear-gradient(#d3c8b6,#b8ab96)}
.quote{left:382px;width:402px;font-size:10.1px;line-height:19px;color:var(--ink)}
.quote-date{font-size:10px;color:var(--heading-red);right:40px;text-align:right}

.footer-nav{left:0;top:1140px;width:800px;height:36px;background:#d3c2a2}
.footer-nav .nav-item{height:36px;line-height:36px}
.copyright{left:0;top:1176px;width:800px;height:24px;background:#bca883;font-size:9px;text-align:center;line-height:24px;color:var(--ink)}
</style>
</head>
<body>

<header>
  <div class="abs top-bar">
    <span class="abs welcome">welcome to www.kornhaus.example</span>
    <span class="abs account">Login<span class="sep">|</span>Register here</span>
  </div>

  <svg class="abs logo-banner" viewBox="0 0 232 120" aria-hidden="true">
    <defs>
      <linearGradient id="bannerFill" x1="0" y1="0" x2="0" y2="1">
        <stop offset="0" stop-color="#6b3810"/>
        <stop offset="0.55" stop-color="#8a5126"/>
        <stop offset="1" stop-color="#e9dcc6"/>
      </linearGradient>
      <linearGradient id="bannerShine" x1="0" y1="0" x2="0" y2="1">
        <stop offset="0" stop-color="#ffffff"/>
        <stop offset="1" stop-color="#b98a5e"/>
      </linearGradient>
    </defs>
    <path d="M0 0H232V75L116 120L0 75Z" fill="url(#bannerFill)"/>
    <rect x="0" y="0" width="232" height="14" fill="url(#bannerShine)"/>
  </svg>
  <div class="abs logo-name">KORNHAUS</div>

  <div class="abs cart">
    <svg width="25" height="23" viewBox="0 0 25 23" aria-hidden="true">
      <path d="M1 2H5L8 15H21L24 6H7" fill="none" stroke="#222" stroke-width="2"/>
      <circle cx="10" cy="19.5" r="2" fill="#222"/><circle cx="19" cy="19.5" r="2" fill="#222"/>
    </svg>
    <span>My cart 0 item(s)</span>
  </div>
  <div class="abs mini-search">Search
    <svg width="22" height="17" viewBox="0 0 22 17" aria-hidden="true">
      <circle cx="8" cy="7" r="5" fill="none" stroke="#333" stroke-width="2"/>
      <path d="M12 10L19 15" stroke="#333" stroke-width="3"/>
    </svg>
  </div>

  <div class="abs search-label">Search</div>
  <div class="abs search-field"></div>
  <div class="abs search-btn">Search</div>

  <nav class="abs main-nav">
    <span class="nav-item active" style="left:84px">Home</span>
    <span class="nav-item" style="left:180px">About Us</span>
    <span class="nav-item" style="left:293px">Bread Mix</span>
    <span class="nav-item" style="left:403px">Recipes</span>
    <span class="nav-item" style="left:527px">Consumer choice</span>
    <span class="nav-item" style="left:669px">Contact us</span>
  </nav>
</header>

<section class="abs hero">
  <div class="abs hero-photo" role="img" aria-label="Basket of assorted seeded bread loaves and rolls with wheat ears"></div>
  <div class="abs hero-slices" role="img" aria-label="Faded sliced white bread loaf"></div>
  <h1 class="abs hero-title">Lorem ipsum dolor</h1>
  <p class="abs hero-text">sed do eiusmod tempor incididunt ut labore et dolore magna aliqua. Ut enim ad minim veniam, quis nostrud exercitation ullamco laboris nisi ut aliquip ex ea commodo consequat</p>
  <div class="abs hero-price">$25.50</div>
  <svg class="abs hero-arrows" width="95" height="42" viewBox="0 0 95 42" aria-label="Previous and next">
    <path d="M4 12L16 3V8H28C38 8 42 16 42 22C42 30 36 36 28 36H14V29H28C32 29 35 26 35 22C35 18 32 15 28 15H16V21Z" fill="#7a5a3a"/>
    <path d="M91 12L79 3V8H67C57 8 53 16 53 22C53 30 59 36 67 36H81V29H67C63 29 60 26 60 22C60 18 63 15 67 15H79V21Z" fill="#7a5a3a"/>
  </svg>
  <svg class="abs ribbon" width="104" height="76" viewBox="0 0 104 76" aria-label="New Order">
    <path d="M104 0V76H0Z" fill="#111"/>
    <text x="70" y="55" transform="rotate(-36 70 55)" text-anchor="middle" font-family="Sorts Mill Goudy, Georgia, serif" font-size="15" fill="#fff">New Order</text>
  </svg>
</section>

<main>
  <h2 class="abs welcome-title">Welcome to Our Website</h2>
  <div class="abs stay">
    <span>Stay with us</span>
    <i class="social" style="left:132px"></i>
    <i class="social" style="left:162px"></i>
    <i class="social" style="left:193px"></i>
    <i class="social" style="left:224px"></i>
  </div>

  <h3 class="abs section-title" style="left:18px;top:578px">Today’s Special Recipes</h3>
  <div class="abs photo-frame" style="left:18px;top:612px;width:142px;height:140px">
    <div class="photo-fill" role="img" aria-label="Plate of sliced sweet bread with chocolate spread beside a red flower" style="background:radial-gradient(ellipse at 60% 55%,#f2dca8 0%,#c9b47a 45%,#9fb06a 75%,#f3eee4 100%)"></div>
  </div>
  <p class="abs recipe-text">I must explain to you how all this mistaken idea of denouncing pleasure and praising pain was born and I will give you a complete account of the system, and expound the actual teachings of the great explorer of the truth, the master-builder of human happiness. No one rejects, dislikes, or avoids pleasure itself, because it is pleasure, but because those who do not know how to ...</p>
  <div class="abs dark-btn" style="left:392px;top:744px;width:62px">Read more...</div>

  <div class="abs v-line" style="left:488px;top:585px;height:190px"></div>

  <h3 class="abs section-title" style="left:512px;top:578px">Consumer choice</h3>
  <div class="abs pager" style="left:745px;top:584px">◀▶</div>
  <div class="abs thumb" style="left:515px;top:611px" role="img" aria-label="Bowl of cherry tomatoes"><div class="photo-fill" style="background:radial-gradient(circle at 40% 45%,#c6452c,#8a5a3c 55%,#e7dccb)"></div></div>
  <div class="abs thumb" style="left:605px;top:611px" role="img" aria-label="Basket of bread rolls"><div class="photo-fill" style="background:radial-gradient(circle at 50% 50%,#d7a978,#a97a52 55%,#e9dfcf)"></div></div>
  <div class="abs thumb" style="left:695px;top:611px" role="img" aria-label="Glazed pastry on a patterned plate"><div class="photo-fill" style="background:radial-gradient(circle at 50% 50%,#d88c3a,#c9a07a 50%,#efe2d6)"></div></div>
  <div class="abs thumb" style="left:515px;top:692px" role="img" aria-label="Bowl of cherry tomatoes"><div class="photo-fill" style="background:radial-gradient(circle at 40% 45%,#c6452c,#8a5a3c 55%,#e7dccb)"></div></div>
  <div class="abs thumb" style="left:605px;top:692px" role="img" aria-label="Basket of bread rolls"><div class="photo-fill" style="background:radial-gradient(circle at 50% 50%,#d7a978,#a97a52 55%,#e9dfcf)"></div></div>
  <div class="abs thumb" style="left:695px;top:692px" role="img" aria-label="Glazed pastry on a patterned plate"><div class="photo-fill" style="background:radial-gradient(circle at 50% 50%,#d88c3a,#c9a07a 50%,#efe2d6)"></div></div>

  <h3 class="abs section-title" style="left:18px;top:776px">Bread Mix</h3>
  <div class="abs pager" style="left:745px;top:793px">◀▶</div>

  <div class="abs mix photo-frame" style="left:18px;top:808px">
    <div class="photo-fill" role="img" aria-label="Sliced brown bread loaf on a plate" style="background:linear-gradient(160deg,#efe4d4 0%,#b07a48 45%,#8b5530 65%,#e8d7c6 100%)"></div>
    <svg class="price-tab" viewBox="0 0 58 28" aria-hidden="true"><path d="M0 0H58V16L29 28L0 16Z" fill="#6e3d12"/></svg>
    <div class="price-tab"><b>$25</b></div>
  </div>
  <div class="abs mix photo-frame" style="left:175px;top:808px">
    <div class="photo-fill" role="img" aria-label="Sliced brown bread loaf on a plate" style="background:linear-gradient(160deg,#f3ebe0 0%,#c9a383 45%,#b08a6b 65%,#efe2d6 100%)"></div>
    <svg class="price-tab" viewBox="0 0 58 28" aria-hidden="true"><path d="M0 0H58V16L29 28L0 16Z" fill="#6e3d12"/></svg>
    <div class="price-tab"><b>$25</b></div>
  </div>
  <div class="abs mix photo-frame" style="left:330px;top:808px">
    <div class="photo-fill" role="img" aria-label="Sliced brown bread loaf on a plate" style="background:linear-gradient(160deg,#f3ebe0 0%,#c9a383 45%,#b08a6b 65%,#efe2d6 100%)"></div>
    <svg class="price-tab" viewBox="0 0 58 28" aria-hidden="true"><path d="M0 0H58V16L29 28L0 16Z" fill="#6e3d12"/></svg>
    <div class="price-tab"><b>$25</b></div>
  </div>
  <div class="abs mix photo-frame" style="left:486px;top:808px">
    <div class="photo-fill" role="img" aria-label="Sliced brown bread loaf on a plate" style="background:linear-gradient(160deg,#f3ebe0 0%,#c9a383 45%,#b08a6b 65%,#efe2d6 100%)"></div>
    <svg class="price-tab" viewBox="0 0 58 28" aria-hidden="true"><path d="M0 0H58V16L29 28L0 16Z" fill="#6e3d12"/></svg>
    <div class="price-tab"><b>$25</b></div>
  </div>
  <div class="abs mix photo-frame" style="left:641px;top:808px">
    <div class="photo-fill" role="img" aria-label="Sliced brown bread loaf on a plate" style="background:linear-gradient(160deg,#f3ebe0 0%,#c9a383 45%,#b08a6b 65%,#efe2d6 100%)"></div>
    <svg class="price-tab" viewBox="0 0 58 28" aria-hidden="true"><path d="M0 0H58V16L29 28L0 16Z" fill="#6e3d12"/></svg>
    <div class="price-tab"><b>$25</b></div>
  </div>

  <div class="abs h-line" style="left:18px;top:935px;width:748px"></div>

  <h3 class="abs section-title" style="left:18px;top:953px">Feed back</h3>
  <span class="abs label" style="left:30px;top:988px">Name</span>
  <div class="abs field" style="left:77px;top:987px;height:22px"></div>
  <span class="abs label" style="left:30px;top:1020px">e-Mail</span>
  <div class="abs field" style="left:77px;top:1019px;height:22px"></div>
  <span class="abs label" style="left:19px;top:1053px">Message</span>
  <div class="abs field" style="left:77px;top:1052px;height:46px"></div>
  <div class="abs dark-btn" style="left:125px;top:1108px;width:70px;height:21px;line-height:19px;font-size:12px;border-radius:8px">Submit</div>

  <div class="abs v-line" style="left:277px;top:948px;height:187px"></div>

  <h3 class="abs section-title" style="left:307px;top:953px">Testimonial</h3>
  <div class="abs avatar" style="left:312px;top:990px" role="img" aria-label="Customer avatar placeholder"></div>
  <p class="abs quote" style="top:988px">I must explain to you how all this mistaken idea of denouncing pleasure and praising pain was born and I will give you a complete account of the system,</p>
  <span class="abs quote-date" style="top:1031px">12-11-2011 &nbsp;- &nbsp;July</span>
  <div class="abs h-line" style="left:378px;top:1046px;width:397px"></div>
  <div class="abs avatar" style="left:312px;top:1055px" role="img" aria-label="Customer avatar placeholder"></div>
  <p class="abs quote" style="top:1056px;left:384px">I must explain to you how all this mistaken idea of denouncing pleasure and praising pain was born and I will give you a complete account of the system,</p>
  <span class="abs quote-date" style="top:1097px;right:37px">12-11-2011 &nbsp;- &nbsp;July</span>
</main>

<footer>
  <nav class="abs footer-nav">
    <span class="nav-item" style="left:117px">Home</span>
    <span class="nav-item" style="left:212px">About Us</span>
    <span class="nav-item" style="left:325px">Bread Mix</span>
    <span class="nav-item" style="left:436px">Recipes</span>
    <span class="nav-item" style="left:560px">Consumer choice</span>
    <span class="nav-item" style="left:701px">Contact us</span>
  </nav>
  <div class="abs copyright">Copyright © 2011. www.kornhaus.example</div>
</footer>

</body>
</html>
```